Kestrel Estate Services, TheFrostGroup Real Estate Advisors

We need a letterhead for both stationery and web site for a company called "Kestrel Estate Services" TheFrostGroup Real Estate Advisors.
We assist individuals that are settling an estate. We offer assistance with selling the real estate, cleanout, repair, auction, & staging. I want the letterhead in colors that communicate professionalism, & reliable

Target Market(s)

Executors, & Attorneys

Industry/Entity Type

Real Estate

Font styles to use
Serif
Sans Serif

Requirements
Must have
• At the bottom of the page in a small font it should read.
• Halden & Pike Partners / 2718 Cedar Glen Rd. Harborton, OR 97871 / 541.555.0147
• Not Intended to Solicit Properties Under Contract

```html
<!DOCTYPE html>
<html lang="en">
<head>
<meta charset="utf-8">
<title>Kestrel Estate Services Letterhead</title>
<link rel="stylesheet" href="https://fonts.googleapis.com/css2?family=Montserrat:wght@700&family=Oswald:wght@400&family=Quattrocento:wght@400&display=swap">
<style>
  :root {
    --navy: #1e3d52;
    --steel: #8a9ea8;
    --footer-grey: #7f959e;
    --body-text: #666a6d;
    --white: #ffffff;
    --footer-text: #e6ecef;
  }
  * { margin: 0; padding: 0; box-sizing: border-box; }
  html, body { width: 927px; height: 1200px; overflow: hidden; background: var(--white); }
  .letterhead { position: relative; width: 927px; height: 1200px; background: var(--white); overflow: hidden; }

  .masthead { position: absolute; top: 0; left: 0; width: 927px; height: 117px; background: var(--navy); }
  .masthead-rule { position: absolute; top: 117px; left: 0; width: 927px; height: 6px; background: var(--steel); }
  .brand-name {
    position: absolute; left: 33px; top: 38px;
    font-family: "Montserrat", sans-serif; font-weight: 700; font-size: 22px;
    letter-spacing: 2.4px; color: var(--white); line-height: 1; text-transform: uppercase;
    white-space: nowrap;
  }
  .brand-divider { position: absolute; left: 33px; top: 66px; width: 352px; height: 1px; background: var(--white); opacity: .85; }
  .brand-tagline {
    position: absolute; left: 47px; top: 74px;
    font-family: "Oswald", sans-serif; font-size: 11px; letter-spacing: 4.3px;
    color: var(--white); line-height: 1; text-transform: uppercase; white-space: nowrap;
  }

  .letter {
    font-family: "Quattrocento", serif; font-size: 15px; line-height: 18.2px;
    color: var(--body-text);
  }
  .letter > * { position: absolute; left: 66px; width: 800px; white-space: nowrap; }
  .letter-date { top: 235px; }
  .recipient { top: 271px; }
  .salutation { top: 362px; }
  .body-1 { top: 418px; }
  .body-2 { top: 581px; }
  .body-3 { top: 763px; }
  .closing { top: 853px; }
  .signature { top: 982px; }

  .footer { position: absolute; left: 0; bottom: 0; width: 927px; height: 80px; }
  .footer-line {
    position: absolute; left: 0; width: 927px; text-align: center;
    font-family: "Oswald", sans-serif; font-size: 10px; letter-spacing: 3.1px;
    color: var(--footer-text); text-transform: uppercase; line-height: 1; white-space: nowrap;
  }
  .footer-address { top: 1157px; }
  .footer-notice { top: 1172px; }
</style>
</head>
<body>
<div class="letterhead">
  <header>
    <div class="masthead">
      <div class="brand-name">Kestrel Estate Services</div>
      <div class="brand-divider"></div>
      <div class="brand-tagline">TheFrostGroup Real Estate Advisors</div>
    </div>
    <div class="masthead-rule"></div>
  </header>

  <main class="letter">
    <p class="letter-date">Month xx,xxxx</p>
    <p class="recipient">Name<br>Organization<br>Address<br>City, State, Zip</p>
    <p class="salutation">Dear_________,</p>
    <p class="body-1">Lorem ipsum dolor sit amet, consectetur adipiscing elit. Cras gravida mattis felis id tincidunt. Suspendisse<br>ullamcorper justo sapien, eu venenatis lorem consectetur id. Donec dignissim orci tellus, ut dignissim ante<br>egestas non. In nec vehicula lacus. Vivamus facilisis, turpis at aliquam fringilla, nunc erat vestibulum nibh, ac<br>sollicitudin metus enim id tellus. Sed semper dolor ac condimentum semper. Aenean lectus sapien, laoreet et<br>fringilla at, sodales et justo. Nunc ornare, ante a congue pretium, massa ipsum consectetur massa, ut auctor<br>neque leo vulputate sem. Quisque placerat turpis sit amet tellus bibendum dignissim. Nulla vel metus nec justo<br>pharetra volutpat sed ac lectus. Nulla commodo cursus tempus. Ut fermentum libero tortor, a gravida nisi<br>gravida in. Ut gravida orci ut sem molestie facilisis.</p>
    <p class="body-2">Aliquam dignissim, neque ut dignissim vestibulum, erat metus imperdiet mauris, vitae viverra eros felis vitae<br>nisl. Sed dapibus turpis id lectus elementum finibus. Vivamus auctor, risus sit amet auctor auctor, nisi nulla<br>ultrices odio, non ornare urna nisl eget nunc. Duis ut urna hendrerit, elementum velit eget, vehicula elit. Fusce<br>venenatis accumsan diam nec lobortis. Pellentesque a nisl eget sem elementum sollicitudin. Mauris sagittis<br>condimentum nunc nec ullamcorper. Curabitur non accumsan ligula, eget fermentum sapien. In sed magna<br>nec libero iaculis tempus et eget arcu. Suspendisse ultricies rutrum libero nec cursus. Etiam vitae enim eget<br>felis ullamcorper lobortis. Etiam eros sem, rutrum non nisi et, vehicula blandit nibh. Interdum et malesuada<br>fames ac ante ipsum primis in faucibus. Praesent dignissim egestas felis, eget commodo lorem blandit vitae. In<br>consectetur cursus dui, quis luctus justo finibus eget.</p>
    <p class="body-3">In augue leo, sagittis vel dignissim quis, maximus non ligula. Quisque ac dolor tempus libero sodales volutpat.<br>Proin lacinia orci ut volutpat ullamcorper. Mauris fermentum viverra convallis. Quisque congue quam ante, ac<br>vehicula est volutpat quis. Curabitur porttitor dui a pharetra convallis. Nullam rhoncus felis enim, in tempus<br>orci interdum ut.</p>
    <p class="closing">Sincerely,</p>
    <p class="signature">John Doe</p>
  </main>

  <footer>
    <svg class="footer" width="927" height="80" viewBox="0 0 927 80" aria-hidden="true">
      <polygon points="0,8 68,22 927,22 927,80 0,80" fill="var(--footer-grey)"/>
    </svg>
    <p class="footer-line footer-address">Halden &amp; Pike Partners / 2718 Cedar Glen Rd. Harborton, OR 97871 / 541.555.0147</p>
    <p class="footer-line footer-notice">Not Intended to Solicit Properties Under Contract</p>
  </footer>
</div>
</body>
</html>
```